Rapidly Growing Small Management Consulting Firm seeking Letterhead/Business Proposal Template

Small Management Consulting Firm in need of Stationery/Business Proposal Template/Business Card for communicating and corresponding to formal Government Statement of Work (SOWs) Request for Proposals (RFP), general business correspondences and engagements with private industry clients. I am in need of company letterhead/stationery and proposal package of documents that follow the same theme in MS Word or a format that I can easily edit to readily respond quickly to business inquiries.

Consulting Firm small business start-up. Minority woman-owned rapidly growing consulting firm based in Washington, DC metropolitan area with a target market of the local and federal government. Would like see some area government images such as buildings or monuments. Looking for something eye-catching and creates a strong presence. The final design should communicate our numerous service offerings.

Target Market(s)

Local State, Federal Government and Private Industry clients and (Business-to-Business (B2B)

Industry/Entity Type

Management Consulting

Number of Pages Required

3 page

Font styles to use
Serif
Sans Serif
Other font styles liked:
• Arial, Calibri, Cambria and Times Roman

Colors
3176b5
ffffff
ec1f27
85abd2
cfdeed

Requirements
Must have
• WEBSITE: PLEASE TAKE A LOOK AT SOME OF THE IMAGES PROVIDED. I AM EXTREMELY INTERESTED IN IMAGE #16. IF SOMETHING LIKE THIS CAN BE DONE FOR THE WEBSITE LANDING PAGE WITH A WASHINGTON, DC OR MONUMENTAL BACKDROP OR BACKGROUND. WOULD LIKE TO USE THE IMAGE OF AFRICAN AMERICAN WOMAN IN FRONT ALONG WITH ANY OTHER DIVERSE STOCK IMAGES BEHIND HER. PLEASE USE A LIGHTER AND BRIGHTER BACKGROUND.
• FOR WEBSITE IMAGE INSPIRATION
• PLEASE TAKE A LOOK @ http://www.tendralux.com/
• http://vamplirio.net/wp-demo/lawfirm/practice-area-01/
• Website: I would like to see general information pages such as Home Page, About US, Services Offered and Careers and Contact Us pages. Must have consistent theme in line with existing Capability Statement.
• FOR COMPANY LETTERHEAD/PROPOSAL/PRESENTATION PAGES:
• MUST FOLLOW SAME THEME. MUST BE IN MS WORD OR FORM THAT CAN BE EASILY EDITABLE. PLEASE SEE UPLOADED "PROPOSAL-PRESENTATION COVER PAGE" IMAGES FOR ADDITIONAL INSPIRATION. I VERY MUCH LIKE IMAGES PPCP #4 AND PPCP#5.
• Must include a multi-use company cover page for proposals and business presentations.
• For letterhead and please incorporate existing logo into design. Company colors gray and blue. Must have the functionality to format page numbering, consistent company information throughout document in headers and footers and will need a customizable company cover page that can be used for proposals and presentations.
• Please do not make the header and footer borders too large as I have to be able to input company information into the space. Some responses have set page limits so it is very important to preserve as much space as possible.
• Please use updated company address: 482 Harrowgate Lane, Bel Alton, MD 20611
Nice to have
• Illustration of images that show professional women and minority (african-american) woman in business or professional settings. Women business owners preferably. Classic and very professional appearance. Even though we are a small firm I would like to design to give the impression and feel of doing business with a large management firm. Or large firm appeal. Also incorporate image of contract signing as our main line of business is acquisitions which is much like the services of a law firm.
• 01/21/17. Added some images of women business owner examples.
Should not have
• Misspellings, images of professionals without business attire.

```html
<!DOCTYPE html>
<html lang="en">
<head>
<meta charset="utf-8">
<title>Marlowe Acquisition Advisors – Letterhead</title>
<link href="https://fonts.googleapis.com/css2?family=Roboto+Condensed:wght@400;700&display=swap" rel="stylesheet">
<style>
  :root {
    --backdrop: #e9eaeb;
    --paper: #ffffff;
    --brand-blue: #00427f;
    --brand-gray: #5f6468;
    --ink: #222222;
  }
  html, body {
    margin: 0;
    padding: 0;
    width: 1200px;
    height: 1200px;
    overflow: hidden;
    background: var(--backdrop);
    font-family: "Roboto Condensed", "Arial Narrow", sans-serif;
  }
  .canvas {
    position: relative;
    width: 1200px;
    height: 1200px;
  }
  .letterhead-frame {
    position: absolute;
    left: 150px;
    top: 17px;
    width: 900px;
    height: 1165px;
  }
  .letterhead {
    position: absolute;
    left: 0;
    top: 0;
    width: 786px;
    height: 1017px;
    background: var(--paper);
    transform: scale(1.1455);
    transform-origin: 0 0;
    overflow: hidden;
  }
  .header-band {
    position: absolute;
    left: 0;
    top: 0;
    width: 100%;
    height: 20px;
    background: var(--brand-blue);
  }
  .header-rule {
    position: absolute;
    left: 0;
    top: 24px;
    width: 100%;
    height: 3px;
    background: var(--brand-gray);
  }
  .footer-rule {
    position: absolute;
    left: 0;
    bottom: 28px;
    width: 100%;
    height: 3px;
    background: var(--brand-gray);
  }
  .footer-band {
    position: absolute;
    left: 0;
    bottom: 0;
    width: 100%;
    height: 24px;
    background: var(--brand-blue);
  }
  .brand-mark {
    position: absolute;
    left: 120px;
    top: 102px;
    display: flex;
    align-items: center;
    gap: 8px;
    color: var(--brand-blue);
    font-weight: 700;
    font-size: 30px;
    letter-spacing: 0.5px;
  }
  .brand-mark .dot {
    width: 14px;
    height: 14px;
    border-radius: 50%;
    background: var(--brand-blue);
  }
  .contact-block {
    position: absolute;
    left: 565px;
    top: 40px;
    height: 126px;
    border-left: 1.5px solid var(--brand-blue);
    padding-left: 15px;
  }
  .contact-name {
    margin: 8px 0 0;
    font-weight: 700;
    font-size: 21px;
    letter-spacing: 2.5px;
    color: var(--ink);
    line-height: 1;
  }
  .contact-tagline {
    margin: 3px 0 0;
    font-size: 6px;
    letter-spacing: 1px;
    color: var(--brand-blue);
  }
  .contact-list {
    list-style: none;
    margin: 14px 0 0;
    padding: 0;
    font-size: 11px;
    color: var(--ink);
  }
  .contact-list li {
    display: flex;
    align-items: center;
    gap: 4px;
    height: 14.5px;
  }
  .contact-list svg {
    width: 11px;
    height: 11px;
    flex: none;
  }
  .contact-address {
    margin: 8px 0 0;
    font-size: 11px;
    line-height: 13px;
    color: var(--brand-blue);
    font-style: normal;
  }
</style>
</head>
<body>
<div class="canvas">
  <div class="letterhead-frame">
    <div class="letterhead">
      <div class="header-band"></div>
      <div class="header-rule"></div>

      <div class="brand-mark">
        <span class="dot"></span>
        <span>Marlowe</span>
      </div>

      <div class="contact-block">
        <p class="contact-name">MARLOWE</p>
        <p class="contact-tagline">ACQUISITION ADVISORS</p>
        <ul class="contact-list">
          <li>
            <svg viewBox="0 0 12 12" aria-hidden="true"><rect x="0.5" y="0.5" width="11" height="11" rx="1.5" fill="none" stroke="#00427f"/><path d="M3,5 Q6,2 9,5 L8.5,6 L7,5.5 V5 H5 V5.5 L3.5,6 Z M4,7 H8 V9 H4 Z" fill="#00427f"/></svg>
            <span>202-555-0147</span>
          </li>
          <li>
            <svg viewBox="0 0 12 12" aria-hidden="true"><rect x="0.5" y="0.5" width="11" height="11" rx="1.5" fill="none" stroke="#00427f"/><rect x="2.5" y="3.5" width="7" height="5" fill="none" stroke="#00427f"/><path d="M2.5,3.5 L6,6.5 L9.5,3.5" fill="none" stroke="#00427f"/></svg>
            <span>info@marloweadvisors.com</span>
          </li>
          <li>
            <svg viewBox="0 0 12 12" aria-hidden="true"><rect x="0.5" y="0.5" width="11" height="11" rx="1.5" fill="none" stroke="#00427f"/><circle cx="6" cy="6" r="3.5" fill="none" stroke="#00427f"/><path d="M2.5,6 H9.5 M6,2.5 V9.5" stroke="#00427f" stroke-width="0.8"/></svg>
            <span>www.marloweadvisors.com</span>
          </li>
        </ul>
        <address class="contact-address">482 Harrowgate Lane<br>Bel Alton, MD 20611</address>
      </div>

      <div class="footer-rule"></div>
      <div class="footer-band"></div>
    </div>
  </div>
</div>
</body>
</html>
```